Business Card Design

I am a Building Surveyor and run my own Building Consultat company, providing professional advice and services to builders, architects, designers, owners, etc.

Industry/Entity Type

Business

Contact Information for Business Card

Dorwen Halket BBldgSurv (Hons)
Managing Director

57 Quillon Rise, Marrick Heights WA 6148
Mobile 0438 271 594
Email Dorwen.halket@tarnwellpq.com

Requirements
Must have
• I would like the back of the business card to be one colour (a shade of either black or maroon, matching the colours of my logo). Positioned in the centre on the back of the business card is to be my logo.

The front of the card is to be white, with my contact information in either black or maroon. The ADBldgSurv after my name should be in a smaller font size than my name. I would also like a small logo somewhere on this side of the card.

```html
<!DOCTYPE html>
<html lang="en">
<head>
<meta charset="utf-8">
<title>Tarnwell Building Consultants – Business Card</title>
<link rel="stylesheet" href="https://fonts.googleapis.com/css2?family=Cinzel:wght@400;600&display=swap">
<style>
  :root {
    --maroon: #6e1a1a;
    --maroon-soft: #8a2a2a;
    --black: #0b0b0b;
    --charcoal: #1a1a1a;
    --grey-text: #5c5c5c;
    --silver-light: #f4f4f4;
    --silver-dark: #c6c6c6;
    --ink: #2b2b2b;
    --page: #ffffff;
  }
  * { box-sizing: border-box; margin: 0; padding: 0; }
  html, body {
    width: 1200px; height: 1000px; overflow: hidden;
    background: var(--page);
    font-family: "Cinzel", serif;
  }
  .canvas {
    position: relative; width: 1200px; height: 1000px;
  }
  .card {
    position: absolute; left: 250px; width: 700px; height: 400px;
    overflow: hidden;
    box-shadow: 0 8px 24px rgba(0,0,0,0.25);
  }

  /* Back of card */
  .card--back {
    top: 70px;
    background: linear-gradient(135deg, var(--charcoal), var(--black));
    display: flex; align-items: center; justify-content: center; gap: 26px;
  }
  .brand-mark {
    width: 96px; height: 96px; border-radius: 50%;
    border: 6px solid var(--maroon);
    flex-shrink: 0;
  }
  .brand-name {
    color: #6a6a6a; font-weight: 400; text-transform: uppercase;
    line-height: 1.1;
  }
  .brand-name__main { display: block; font-size: 50px; letter-spacing: 1px; }
  .brand-name__sub { display: block; font-size: 17px; letter-spacing: 3px; text-align: center; margin-top: 4px; }

  /* Front of card */
  .card--front {
    top: 530px;
    background: linear-gradient(100deg, var(--silver-dark) 0%, var(--silver-light) 30%, #e6e6e6 65%, var(--silver-dark) 100%);
  }
  .front-band {
    position: absolute; left: 0; right: 0; bottom: 0; height: 56px;
    background: var(--black);
  }
  .front-logo {
    position: absolute; left: 48px; top: 62px; width: 170px;
    display: flex; flex-direction: column; align-items: center; gap: 12px;
  }
  .front-logo .brand-mark { width: 140px; height: 140px; border-width: 9px; }
  .front-logo__name { color: var(--maroon); font-size: 18px; letter-spacing: 2px; text-transform: uppercase; }

  .contact { position: absolute; left: 262px; top: 62px; color: var(--ink); }
  .contact__name {
    color: var(--maroon); font-weight: 600; font-size: 25px; text-transform: uppercase; letter-spacing: 1px;
  }
  .contact__credential { font-size: 16px; font-weight: 400; margin-left: 6px; letter-spacing: 0.5px; }
  .contact__role { font-size: 21px; text-transform: uppercase; color: var(--ink); margin-top: 2px; }
  .contact__list { list-style: none; margin-top: 26px; }
  .contact__item {
    display: flex; align-items: center; gap: 12px;
    font-size: 18px; letter-spacing: 0.5px; margin-bottom: 12px;
  }
  .contact__item--email { font-size: 15px; text-transform: uppercase; }
  .icon { width: 30px; height: 30px; flex-shrink: 0; }
</style>
</head>
<body>
<main class="canvas">

  <section class="card card--back" aria-label="Back of business card">
    <span class="brand-mark" aria-hidden="true"></span>
    <p class="brand-name">
      <span class="brand-name__main">Tarnwell</span>
      <span class="brand-name__sub">Building Consultants</span>
    </p>
  </section>

  <section class="card card--front" aria-label="Front of business card">
    <div class="front-logo">
      <span class="brand-mark" aria-hidden="true"></span>
      <span class="front-logo__name">Tarnwell</span>
    </div>

    <div class="contact">
      <h1 class="contact__name">Dorwen Halket<span class="contact__credential">ADBldgSurv</span></h1>
      <p class="contact__role">Director</p>
      <ul class="contact__list">
        <li class="contact__item">
          <svg class="icon" viewBox="0 0 30 30" aria-hidden="true">
            <circle cx="15" cy="15" r="13" fill="none" stroke="var(--maroon)" stroke-width="2.5"/>
            <path d="M8 15 L15 9 L22 15 M10 14 V21 H20 V14" fill="none" stroke="var(--maroon)" stroke-width="1.6"/>
          </svg>
          57 Quillon Rise, Marrick Heights WA 6148
        </li>
        <li class="contact__item">
          <svg class="icon" viewBox="0 0 30 30" aria-hidden="true">
            <circle cx="15" cy="15" r="13" fill="none" stroke="var(--maroon)" stroke-width="2.5"/>
            <path d="M11 8 C9 9 8.5 12 10.5 16 C12.5 20 16 22.5 18.5 21.5 L20 19.5 L17.5 17 L16 18 C14.5 17.5 12.5 15 12 13.5 L13 12 L11 8 Z" fill="var(--maroon)"/>
          </svg>
          0438 271 594
        </li>
        <li class="contact__item contact__item--email">
          <svg class="icon" viewBox="0 0 30 30" aria-hidden="true">
            <circle cx="15" cy="15" r="13" fill="none" stroke="var(--maroon)" stroke-width="2.5"/>
            <rect x="8.5" y="10.5" width="13" height="9" fill="none" stroke="var(--maroon)" stroke-width="1.5"/>
            <path d="M8.5 10.5 L15 16 L21.5 10.5" fill="none" stroke="var(--maroon)" stroke-width="1.5"/>
          </svg>
          dorwen.halket@tarnwellpq.com
        </li>
      </ul>
    </div>

    <div class="front-band" aria-hidden="true"></div>
  </section>

</main>
</body>
</html>
```